Technology Enablement - One Pager

I need (2) one pager piece of marketing collateral to use as outreach for a service offering. The one pager must have a strong call to action, highlight the pain points the service solves.

```html
<!DOCTYPE html>
<html lang="en">
<head>
<meta charset="utf-8">
<title>Technology Enablement One Pagers</title>
<link href="https://fonts.googleapis.com/css2?family=Montserrat:ital,wght@0,400;0,600;0,700;0,800;1,500&family=Arimo:wght@400;700&display=swap" rel="stylesheet">
<style>
:root{
  --bg:#9a9a9a;
  --paper:#ffffff;
  --mist:#efefef;
  --ink:#222326;
  --navy:#152a55;
  --blue:#0a5bbd;
  --blue-deep:#0947a0;
  --sky:#3d9ee6;
  --night:#12161d;
  --slate:#2a3442;
}
*{box-sizing:border-box;margin:0;padding:0}
html,body{width:675px;height:1200px;overflow:hidden;background:var(--bg)}
body{position:relative;font-family:"Arimo",Arial,sans-serif;color:var(--ink)}
.sheet{position:absolute;left:131px;width:412px;height:580px;background:var(--paper);overflow:hidden}
.sheet--smb{top:13px}
.sheet--trades{top:607px}

.hero{position:absolute;left:0;top:0;width:412px;background:linear-gradient(120deg,#0c1017 0%,#1d2a38 45%,#0f141b 100%)}
.sheet--smb .hero{height:169px}
.sheet--trades .hero{height:143px;background:linear-gradient(110deg,#101319 0%,#262b33 50%,#3a3f47 75%,#1a1d22 100%)}
.title-tab{position:absolute;left:58px;top:0;width:300px;height:25px;background:var(--paper);border-radius:0 0 16px 16px;
  font-family:"Montserrat",sans-serif;font-weight:700;color:var(--blue);font-size:12.5px;text-align:center;line-height:25px}
.sheet--trades .title-tab{left:60px;width:296px}
.headline{position:absolute;font-family:"Montserrat",sans-serif;color:#fff;letter-spacing:.2px}
.sheet--smb .headline{left:28px;top:56px;font-size:16px;font-weight:400;line-height:19px}
.headline strong{color:var(--sky);font-weight:800}
.hero-sub{position:absolute;color:#fff;font-weight:700;font-family:"Arimo",sans-serif}
.sheet--smb .hero-sub{left:30px;top:107px;font-size:9.3px;line-height:11.5px;width:190px}
.trade-list{position:absolute;left:0;width:412px;top:37px;text-align:center;color:#fff;font-family:"Montserrat",sans-serif;font-style:italic;font-weight:500;font-size:8.4px;line-height:10px}
.sheet--trades .headline{left:33px;top:55px;font-size:16.5px;font-weight:800;line-height:19px}
.sheet--trades .hero-sub{left:34px;top:101px;font-size:9px;line-height:11px;width:220px}

h2{font-family:"Arimo",sans-serif;font-weight:700;font-size:7.4px;line-height:9px;color:var(--ink);margin-bottom:3px}
h3{font-weight:400;font-size:6.6px;line-height:8px;color:var(--sky);margin-bottom:2px}
h4{line-height:8px}
p{font-size:4.6px;line-height:5.6px;margin-bottom:3px}
p.strong{font-weight:700}
ul{list-style:none;margin-bottom:3px}
li{font-size:4.6px;line-height:5.7px;padding-left:6px;position:relative}
li::before{content:"";position:absolute;left:0;top:1.4px;width:3.2px;height:3.2px;border:.6px solid var(--sky);border-radius:50%}
.gap{margin-top:7px}

.smb-main{position:absolute;left:27px;top:183px;width:165px}

.offer{position:absolute;left:198px;top:121px;width:214px;height:343px;background:linear-gradient(160deg,#0d63c8,#0a4fae);
  border-top-left-radius:16px;border:3px solid var(--paper);border-right:none;border-bottom:none;color:#fff;padding:11px 12px 0 18px}
.offer h2,.offer p,.offer li{color:#fff}
.offer h2{font-size:7.6px;line-height:9px}
.offer .sub{font-size:6px;line-height:7.5px;font-weight:700;margin:4px 0 3px}
.offer .lead{font-size:5.4px;line-height:6.6px;margin-bottom:2px}
.offer li::before{border-color:#9fd0ff}
.offer h4{font-size:6.2px;font-weight:700;margin-top:3px;margin-bottom:1px}
.tags{display:flex;gap:3px;margin:3px 0 4px;background:linear-gradient(90deg,var(--sky),rgba(61,158,230,0));padding:1px 2px;border-radius:3px}
.tags span{font-size:4.4px;line-height:5.6px;font-weight:700;background:var(--blue-deep);padding:1px 4px;border-radius:4px}
.price{font-family:"Montserrat",sans-serif;font-weight:600;font-size:13px;line-height:16px;margin:2px 0 2px}

.cta{position:absolute;left:205px;top:464px;width:207px;height:116px;background:linear-gradient(180deg,#2b3f63,#1b3064);color:#fff;padding:12px 12px 0 21px}
.cta .lede{font-weight:700;font-size:7.2px;line-height:8.6px}
.cta p{font-size:4.8px;line-height:6px;margin-top:2px;color:#d9e3f5}
.cta .action{font-family:"Arimo",sans-serif;font-weight:700;font-size:11px;line-height:13px;margin-top:7px;color:#fff}

.reality{position:absolute;left:0;top:143px;width:412px;height:139px;background:var(--mist);padding:11px 33px 0 33px;display:flex;gap:20px}
.reality .col-a{width:175px}
.reality .col-b{width:150px}
.focus{display:grid;grid-template-columns:1fr 1fr;gap:5px 8px}
.focus p{margin:0}
.promise{position:absolute;left:32px;top:292px;width:360px}
.promise ul{display:flex;gap:10px}
.promise li{width:70px}
.package{position:absolute;left:19px;top:335px;width:378px;height:125px;background:linear-gradient(170deg,#0c62c6,#0a4fae);border-radius:18px;border:2px solid #3576d0;color:#fff;padding:10px 18px}
.package h2{color:#fff;font-size:7.6px;margin-bottom:1px}
.package .sub{font-size:6px;font-weight:700;line-height:7.5px}
.package-cols{display:flex;gap:10px;margin-top:6px}
.package-cols h4{font-size:6px;font-weight:400;margin-bottom:1px}
.package li,.package p{color:#fff}
.package li::before{border-color:#9fd0ff}
.package .review{width:125px}
.package .receive{width:115px}
.package .cost{padding-left:8px}
.package .cost .price{font-size:11px;line-height:13px;font-family:"Arimo",sans-serif;font-weight:700;margin-bottom:3px}
.audience{position:absolute;left:37px;top:477px;width:350px;display:flex;gap:20px}
.audience .who{width:185px}
.who-grid{display:grid;grid-template-columns:1fr 1fr;gap:4px 10px}
.who-grid li{margin-bottom:3px}
.band{position:absolute;left:0;bottom:0;width:412px;height:33px;background:linear-gradient(90deg,#5f8fc7,#2c4d86 55%,#1d3770);color:#fff;font-weight:700;font-size:8.4px;line-height:33px;text-align:center}
</style>
</head>
<body>

<section class="sheet sheet--smb">
  <div class="hero" role="img" aria-label="Dark technology photo of a glowing circuit board"></div>
  <div class="title-tab">Technology Enablement – SMB</div>
  <h1 class="headline">YOUR <strong>TECHNOLOGY</strong> SHOULDN’T<br>SLOW YOUR BUSINESS DOWN.</h1>
  <p class="hero-sub">We help SMBs turn disconnected tools into systems that actually work.</p>

  <div class="smb-main">
    <h2>The Problem</h2>
    <p>Most growing businesses have plenty of software — but no real system.</p>
    <p>You’ve invested in cloud tools, CRMs, accounting platforms, HR apps, and automation. Yet day-to-day work still feels harder than it should.</p>
    <h3 class="gap">Common pain points</h3>
    <ul>
      <li>Software doesn’t talk to each other</li>
      <li>Key processes live in people’s heads</li>
      <li>Manual work fills the gaps between systems</li>
      <li>Decisions are made without clear data</li>
      <li>Tech choices are made reactively, not strategically</li>
    </ul>
    <h3 class="gap">The result?</h3>
    <p>More effort, more admin, and less return on your software spend.</p>
    <h2 class="gap">What We Do</h2>
    <p>Technology Enablement is about improving how work actually flows through your business.</p>
    <h3>Kestrel helps you:</h3>
    <ul>
      <li>Identify workflow and process gaps</li>
      <li>Find where technology is creating friction (not value)</li>
      <li>Improve adoption of the tools you already pay for</li>
      <li>Clarify where automation and integration will actually help</li>
      <li>Build a practical roadmap tied to real business outcomes</li>
    </ul>
    <h3 class="gap">This is not IT support.</h3>
    <p>It’s operational improvement, using technology as the lever.</p>
    <h2 class="gap">Our Approach Is Different</h2>
    <ul>
      <li>You do not need to switch IT providers</li>
      <li>You do not need to rip and replace systems</li>
      <li>You do not need a long-term contract</li>
    </ul>
    <p class="strong">We start with clarity first.<br>Execution comes later — only where it makes sense.</p>
  </div>

  <div class="offer">
    <h2>Product 1: Technology<br>Enablement Assessment</h2>
    <p class="sub">A 2–4 week, stand-alone engagement</p>
    <p class="lead">We assess your:</p>
    <ul>
      <li>Technology &amp; digital maturity</li>
      <li>Core workflows and handoffs</li>
      <li>Integration and automation opportunities</li>
      <li>Adoption gaps and training needs</li>
      <li>Data, reporting, and KPI visibility</li>
      <li>IT and security posture (at a business level)</li>
    </ul>
    <h4>You receive:</h4>
    <p class="strong" style="margin:0">A prioritized 5–10 item Improvement<br>Roadmap, each with:</p>
    <div class="tags"><span>Business impact</span><span>Relative effort</span><span>ROI potential</span></div>
    <p class="price">Price: $2,500</p>
    <p>No upsell required. No obligation beyond the assessment.</p>
    <h4>Who This Is For</h4>
    <ul>
      <li>Small and mid-sized businesses</li>
      <li>Leadership teams feeling “tech pressure” but lacking a plan</li>
      <li>Companies scaling headcount faster than systems</li>
      <li>Owners tired of guessing which tools to buy next</li>
    </ul>
    <h4>Why Start Here</h4>
    <p style="margin-bottom:1px">Because buying more software without fixing workflows just adds complexity.</p>
    <p class="strong" style="margin-bottom:1px">This assessment gives you</p>
    <ul>
      <li>Clarity instead of opinions</li>
      <li>A roadmap instead of random fixes</li>
      <li>Confidence before spending more money</li>
    </ul>
  </div>

  <div class="cta">
    <p class="lede">Start with insight. Move forward<br>with confidence.</p>
    <p>Let’s identify what’s actually holding your business back — and how to fix it.</p>
    <p class="action">Book a Technology<br>Enablement Assessment</p>
  </div>
</section>

<section class="sheet sheet--trades">
  <div class="hero" role="img" aria-label="Dark photo of a tradesperson with hexagon technology icons"></div>
  <div class="title-tab">Technology Enablement for Trades</div>
  <p class="trade-list">(Electrical, Plumbing, HVAC, Mechanical, Construction)</p>
  <h1 class="headline">YOUR JOBS ARE PHYSICAL. YOUR<br>PROBLEMS AREN’T.</h1>
  <p class="hero-sub">We help trade businesses fix the tech and workflows behind the work.</p>

  <div class="reality">
    <div class="col-a">
      <h2>The Reality in the Trades</h2>
      <p>Trade companies rely on technology more than ever — even if they don’t call it “IT.”</p>
      <p>Scheduling. Estimating. Job tracking. Invoicing. Payroll. Field apps. Most of it works… kind of.</p>
      <ul>
        <li>Office and field systems don’t line up</li>
        <li>Dispatch process is manual or inefficient</li>
        <li>Jobs get quoted one way and invoiced another</li>
        <li>Information is stuck in texts, notebooks, or someone’s phone</li>
        <li>Admin work grows faster than revenue</li>
        <li>Technology decisions fall to “whoever knows computers”</li>
      </ul>
      <p>The work gets done — but it takes more effort than it should.</p>
    </div>
    <div class="col-b">
      <h2>What We Do</h2>
      <p class="strong">Kestrel focuses on:</p>
      <div class="focus">
        <p>How work flows from quote → job → invoice → reporting</p>
        <p>Where manual steps create delays, rework, or missed revenue</p>
        <p>How office and field tools connect (or don’t)</p>
        <p>Why tools aren’t being fully used by crews or admin staff</p>
      </div>
      <p style="margin-top:4px">This is about making the business easier to run — not selling IT jargon.</p>
    </div>
  </div>

  <div class="promise">
    <h2>The Reality in the Trades</h2>
    <ul>
      <li>Low-risk, practical, and clear</li>
      <li>No pressure to replace systems</li>
      <li>No requirement to change IT providers</li>
      <li>Focused on productivity, not tech for tech’s sake</li>
    </ul>
  </div>

  <div class="package">
    <h2>Product 1: Trades Technology Enablement Assessment</h2>
    <p class="sub">A 2–4 week, stand-alone assessment<br>built specifically for trades</p>
    <div class="package-cols">
      <div class="review">
        <h4>We review</h4>
        <ul>
          <li>Job management workflows</li>
          <li>Quoting → scheduling → invoicing flow</li>
          <li>Field tools and adoption gaps</li>
          <li>Office vs field handoffs</li>
          <li>Reporting visibility (jobs, labour, margins)</li>
          <li>Security and data risks (without fear tactics)</li>
        </ul>
      </div>
      <div class="receive">
        <h4>You receive</h4>
        <p style="margin-bottom:1px">A Trades-Specific Improvement Roadmap showing:</p>
        <ul>
          <li>Where time and money are being lost</li>
          <li>What to fix first</li>
          <li>What can wait</li>
          <li>Where automation or integration actually pays off</li>
        </ul>
      </div>
      <div class="cost">
        <p class="price">Price:<br>$2,500</p>
        <p>Straightforward. No obligation beyond the assessment.</p>
      </div>
    </div>
  </div>

  <div class="audience">
    <div class="who">
      <h2>Who This Is For</h2>
      <div class="who-grid">
        <ul>
          <li>Electrical, plumbing, HVAC, mechanical, GC, and construction firms</li>
          <li style="margin-top:5px">Owners feeling buried in admin</li>
        </ul>
        <ul>
          <li>Companies growing past “winging it”</li>
          <li style="margin-top:5px">Trades relying on multiple apps that don’t work well together</li>
        </ul>
      </div>
    </div>
    <div class="why">
      <h2>Why Start With an Assessment</h2>
      <p style="margin-bottom:1px">Because guessing costs more than clarity.<br>This gives you</p>
      <ul>
        <li>A clear plan instead of piecemeal fixes</li>
        <li>Confidence before spending on new tools</li>
        <li>A roadmap aligned to how trades actually work</li>
      </ul>
    </div>
  </div>

  <div class="band">Fix the systems behind the scenes — so the work runs smoother on site</div>
</section>

</body>
</html>
```